Contemporary Elegant Business Card Design for an International Trade Company in the Wine Industry

We need a new business card design for an international trade company in the wine and winemaking industry. The overall feel of the card should be contemporary, upscale, luxurious and elegant. It should communicate confidence and professionalism. The colors should complementary to our logo design (burgundy, gold, and black).
Inspiration: rich velvet tapestry
The card should include the following information:
Business: Corvelle Trading/Shipping, LLC.
Name: Martin R. Obrastow
Title: CEO
Email: marty@corvelletrading.example
Phone: 555-482-1957
www.corvelletrading.example
Reason: We'd like the designers that we requested some additional designs from to still submit designs. Thank you!
Business
Contact Information for Business Card
Title: CEO
Phone: 555-482-1957
www.corvelletrading.example

```html
<!DOCTYPE html>
<html lang="en">
<head>
<meta charset="utf-8">
<title>Corvelle Trading/Shipping — Business Card</title>
<link href="https://fonts.googleapis.com/css2?family=Lato:wght@300;400;700&display=swap" rel="stylesheet">
<style>
  :root {
    --burgundy: #7d1719;
    --burgundy-deep: #5e1012;
    --charcoal: #1f1f1f;
    --charcoal-line: #3a3a3a;
    --gold: #f0a02c;
    --silver: #cfcfcf;
    --paper: #ffffff;
    --backdrop: #e9e6e1;
  }
  * { box-sizing: border-box; margin: 0; padding: 0; }
  html, body { width: 1200px; height: 800px; overflow: hidden; }
  body {
    background: var(--backdrop);
    font-family: "Lato", sans-serif;
    position: relative;
  }
  .card {
    position: absolute;
    top: 245px;
    width: 540px;
    height: 309px;
    overflow: hidden;
    box-shadow: 0 10px 24px rgba(0,0,0,0.22);
  }
  .card--front { left: 40px; }
  .card--back { left: 620px; }
  .card__shapes { position: absolute; inset: 0; }

  .holder { position: absolute; left: 70px; top: 34px; color: var(--paper); }
  .holder__name {
    font-weight: 400;
    font-size: 21px;
    letter-spacing: 0.5px;
    text-transform: uppercase;
    padding-bottom: 6px;
    border-bottom: 2px solid var(--gold);
    display: inline-block;
  }
  .holder__title { font-weight: 300; font-size: 15px; margin-top: 2px; letter-spacing: 0.5px; }

  .contacts { position: absolute; left: 0; top: 118px; width: 328px; list-style: none; }
  .contacts__row {
    position: relative;
    height: 48px;
    display: flex;
    align-items: center;
    padding-left: 40px;
    color: var(--paper);
    font-size: 14px;
    font-weight: 300;
    letter-spacing: 0.3px;
    border-bottom: 1px solid var(--charcoal-line);
  }
  .contacts__row::before {
    content: "";
    position: absolute;
    left: 0; top: 2px; bottom: 2px;
    width: 14px;
    background: var(--gold);
  }
  .contacts__icon { width: 14px; height: 14px; margin-right: 16px; flex: none; }

  .brand {
    position: absolute;
    display: flex;
    flex-direction: column;
    align-items: center;
    gap: 12px;
    text-align: center;
    color: var(--gold);
    font-weight: 700;
  }
  .card--front .brand { left: 358px; top: 78px; width: 176px; }
  .card--back .brand { left: 160px; top: 78px; width: 220px; }
  .brand__mark { width: 58px; height: 58px; background: var(--gold); }
  .brand__name { font-size: 26px; letter-spacing: 1px; line-height: 1; }
  .card--back .brand__name { font-size: 30px; }
  .brand__tagline { font-size: 11px; letter-spacing: 1px; text-transform: uppercase; margin-top: -4px; }
</style>
</head>
<body>

  <section class="card card--front" aria-label="Business card front">
    <svg class="card__shapes" width="540" height="309" viewBox="0 0 540 309">
      <rect width="540" height="309" fill="var(--burgundy)"/>
      <polygon points="0,0 336,0 328,309 0,309" fill="var(--charcoal)"/>
      <polygon points="336,0 346,0 338,309 328,309" fill="var(--gold)"/>
      <polygon points="346,0 354,0 346,309 338,309" fill="var(--silver)"/>
    </svg>

    <div class="holder">
      <h1 class="holder__name">Martin R. Obrastow</h1>
      <p class="holder__title">CEO</p>
    </div>

    <ul class="contacts">
      <li class="contacts__row">
        <svg class="contacts__icon" viewBox="0 0 16 16"><path d="M3 2h3l1.5 3.5-2 1.3a9 9 0 0 0 3.7 3.7l1.3-2L14 10v3a1 1 0 0 1-1 1A11 11 0 0 1 2 3a1 1 0 0 1 1-1z" fill="var(--paper)"/></svg>
        555-482-1957
      </li>
      <li class="contacts__row">
        <svg class="contacts__icon" viewBox="0 0 16 16"><rect x="1" y="3" width="14" height="10" fill="var(--paper)"/><path d="M1 3l7 6 7-6" fill="none" stroke="var(--charcoal)" stroke-width="1.3"/></svg>
        marty@corvelletrading.example
      </li>
      <li class="contacts__row">
        <svg class="contacts__icon" viewBox="0 0 16 16" fill="none" stroke="var(--paper)" stroke-width="1.3"><circle cx="8" cy="8" r="6.5"/><ellipse cx="8" cy="8" rx="2.8" ry="6.5"/><path d="M1.5 8h13"/></svg>
        www.corvelletrading.example
      </li>
    </ul>

    <div class="brand">
      <span class="brand__mark"></span>
      <span class="brand__name">CORVELLE</span>
      <span class="brand__tagline">Trading and Shipping</span>
    </div>
  </section>

  <section class="card card--back" aria-label="Business card back">
    <svg class="card__shapes" width="540" height="309" viewBox="0 0 540 309">
      <rect width="540" height="309" fill="var(--burgundy)"/>
      <polygon points="0,0 22,0 0,90" fill="var(--charcoal)"/>
      <polygon points="22,0 34,0 0,140 0,90" fill="var(--gold)"/>
      <polygon points="34,0 40,0 0,165 0,140" fill="var(--silver)"/>
      <polygon points="478,0 540,0 540,309 446,309" fill="var(--charcoal)"/>
      <polygon points="466,0 478,0 446,309 434,309" fill="var(--gold)"/>
      <polygon points="458,0 466,0 434,309 426,309" fill="var(--silver)"/>
    </svg>

    <div class="brand">
      <span class="brand__mark"></span>
      <span class="brand__name">CORVELLE</span>
      <span class="brand__tagline">Trading and Shipping</span>
    </div>
  </section>

</body>
</html>
```